Minimalist, Flat(Matte) design for a Beef Jerky packaging company. No bullshit company looking for a

Need a packaging design for a new Beef Jerky product(in English). The name of the company is 'Vellorn' and thus the packaging should reflect the bullish, tough, and simple nature of the beef jerky product. The finished product should communicate simplicity, minimalism, yet toughness and strength.

The logo should be simple, with a minimal number of colors , and should be either all white/cream, or have some red as well. Main colors should be white, cream, tinted red, and matte black. I think 4 colors max would be best. The closest example to an existing package style would be Kessip Noir clove cigarettes( image attached).

It will be on a matte black standing pouch package. See image for package type. Package dimensions:

Dimension: Width x Gusset x Height
INCH : 5.125" (W) x 3.125" (G) x 8.125" (H)
MILLIMETER : 130mm (W) x 80mm (G) x 205mm (H)

I don't have anything totally specific so artistic liberty is encouraged, provided the colors are kept to a minimum and looks consistent with the simple nature of the brand and the matte black packaging.

Also attached an existing beef jerky package with a similar style to what we're looking for.

Industry/Entity Type

It Company

Colors
f59195
ffffff

Requirements
Must have
• Low contrast, flat and minimalist design.
Should not have
• A complicated design with many colors. Gawdy/flashy design. Bright colors. High contrast.

```html
<!DOCTYPE html>
<html lang="en">
<head>
<meta charset="utf-8">
<title>Vellorn Peppered Beef Jerky – Pouch Front</title>
<link rel="stylesheet" href="https://fonts.googleapis.com/css2?family=Barlow+Condensed:wght@400;500;600;700&family=Barlow:wght@400;500&display=swap">
<style>
  :root {
    --backdrop: #e4e4e4;
    --pouch-black: #161616;
    --seam-black: #0e0e0e;
    --tinted-red: #e8767c;
    --line-red: #c9656a;
    --white: #f2f2f2;
    --soft-white: #d9d9d9;
  }
  html, body {
    margin: 0;
    padding: 0;
    width: 1200px;
    height: 1000px;
    overflow: hidden;
    background: var(--backdrop);
  }
  .canvas {
    width: 1200px;
    height: 1000px;
    display: block;
  }
  .pouch-body { fill: var(--pouch-black); }
  .zip-seal { stroke: var(--seam-black); stroke-width: 3; fill: none; }
  .brand-mark { fill: var(--white); }
  .tagline {
    font-family: "Barlow", sans-serif;
    font-weight: 500;
    font-size: 12px;
    letter-spacing: 3px;
    fill: var(--soft-white);
  }
  .brand-name {
    font-family: "Barlow Condensed", sans-serif;
    font-weight: 700;
    font-size: 134px;
    fill: var(--tinted-red);
  }
  .flavor-name {
    font-family: "Barlow Condensed", sans-serif;
    font-weight: 600;
    font-size: 46px;
    fill: var(--white);
  }
  .divider-cross { stroke: var(--tinted-red); stroke-width: 1.5; }
  .craft-label {
    font-family: "Barlow", sans-serif;
    font-weight: 400;
    font-size: 15px;
    letter-spacing: 4.5px;
    fill: var(--soft-white);
  }
  .product-type {
    font-family: "Barlow Condensed", sans-serif;
    font-weight: 600;
    font-size: 40px;
    fill: var(--white);
  }
  .chevron-line { stroke: var(--line-red); stroke-width: 1.5; fill: none; }
  .net-weight {
    font-family: "Barlow Condensed", sans-serif;
    font-weight: 500;
    font-size: 14px;
    letter-spacing: 0.5px;
    fill: var(--soft-white);
  }
</style>
</head>
<body>
<svg class="canvas" viewBox="0 0 1200 1000" xmlns="http://www.w3.org/2000/svg">
  <g class="pouch">
    <path class="pouch-body" d="M402 140 H818 Q830 140 830 152 V880 H390 V152 Q390 140 402 140 Z"/>
    <line class="zip-seal" x1="420" y1="235" x2="800" y2="235"/>
    <line class="zip-seal" x1="420" y1="246" x2="800" y2="246"/>
  </g>

  <g class="logo-lockup" text-anchor="middle">
    <rect class="brand-mark" x="585" y="330" width="50" height="50"/>
    <text class="tagline" x="547" y="388">STRONG</text>
    <text class="tagline" x="675" y="388">FLAVOR</text>
  </g>

  <text class="brand-name" x="610" y="518" text-anchor="middle">VELLORN</text>
  <text class="flavor-name" x="610" y="588" text-anchor="middle">PEPPERED</text>

  <g class="divider-cross">
    <line x1="600" y1="620" x2="620" y2="644"/>
    <line x1="620" y1="620" x2="600" y2="644"/>
  </g>

  <text class="craft-label" x="612" y="684" text-anchor="middle">HANDCRAFTED</text>
  <text class="product-type" x="610" y="728" text-anchor="middle">BEEF JERKY</text>

  <polyline class="chevron-line" points="405,668 460,745 610,790 760,745 815,668"/>

  <text class="net-weight" x="610" y="820" text-anchor="middle">NET WT. 3 OZ</text>
</svg>
</body>
</html>
```